Toward Bright Morrow (TWBM) Business Card - company with a mission

Note* The file attached... orange with "Toward Bright MORROW" (in CAPS) is our logo. I am also open to having the text "toward bright morrow" OUTSIDE the orange round logo for business card (so yes, you may take the text out).

The info: (the following info are separate. So either you can use Martin or Helena for now, but that will be 2 separate cards, not together in one card. Thanks!!

Martin K Pardo
202.555.0183
martin@towardbrightmorrow.example
Managing Partner

Helena R Voss
202.555.0147
helena@towardbrightmorrow.example
Managing Partner

Our website: www.towardbrightmorrow.example

TWBM LLC stands for Toward Bright Morrow (non profit arm is called dawn lift foundation)—our business is based out of New York City and has a non-profit arm where for every bar of soap you purchase, we donate a bar (don’t want any designs that limits us to only soap). Currently working with South Africa. We want the focus to be organic/natural soap with a mission.

Looking for a clean, fresh design.

Industry/Entity Type

Non-Profit

Requirements
Must have
• Clean, fresh, refreshing. Design should not be too busy.

```html
<!DOCTYPE html>
<html lang="en">
<head>
<meta charset="utf-8">
<title>Toward Bright Morrow – Business Card</title>
<link rel="stylesheet" href="https://fonts.googleapis.com/css2?family=Questrial&display=swap">
<style>
  :root {
    --charcoal: #3a3a3b;
    --apricot: #f4ae70;
    --apricot-light: #f7bd88;
    --white: #ffffff;
    --backdrop: #ecebe8;
    --shadow: rgba(0, 0, 0, 0.18);
  }
  * { box-sizing: border-box; margin: 0; padding: 0; }
  html, body {
    width: 1200px;
    height: 1000px;
    overflow: hidden;
    background: var(--backdrop);
    font-family: "Questrial", "Century Gothic", sans-serif;
  }
  .sheet {
    position: relative;
    width: 1200px;
    height: 1000px;
  }
  .card {
    position: absolute;
    left: 200px;
    width: 800px;
    height: 457px;
    border-radius: 4px;
    box-shadow: 0 8px 24px var(--shadow);
    overflow: hidden;
  }
  .card--front { top: 30px; background: var(--charcoal); }
  .card--back { top: 513px; }

  /* front */
  .brand-disc {
    position: absolute;
    left: 225px;
    top: 43px;
    width: 370px;
    height: 370px;
    border-radius: 50%;
    background: var(--apricot);
    display: flex;
    flex-direction: column;
    align-items: center;
    justify-content: center;
    color: var(--white);
    text-align: center;
  }
  .brand-name {
    font-size: 34px;
    line-height: 1.15;
    letter-spacing: 1px;
  }
  .brand-name .brand-line--large {
    display: block;
    font-size: 58px;
    letter-spacing: 2px;
  }

  /* back */
  .back-texture {
    position: absolute;
    inset: 0;
    background: radial-gradient(circle at 50% 50%, var(--apricot-light), var(--apricot) 70%);
  }
  .contact-disc {
    position: absolute;
    left: 188px;
    top: 22px;
    width: 412px;
    height: 412px;
    border-radius: 50%;
    background: var(--charcoal);
    color: var(--white);
    text-align: center;
    padding-top: 92px;
  }
  .contact-name {
    color: var(--apricot);
    font-size: 27px;
    letter-spacing: 2px;
  }
  .contact-role {
    font-size: 23px;
    margin-top: 4px;
  }
  .contact-lines {
    list-style: none;
    margin-top: 30px;
    font-size: 19px;
    line-height: 1.6;
  }
  .contact-label { color: var(--apricot); }
  .contact-web {
    margin-top: 20px;
    font-size: 18px;
  }
  .contact-web .accent { color: var(--apricot); }
</style>
</head>
<body>
<main class="sheet">
  <section class="card card--front" aria-label="Card front">
    <div class="brand-disc">
      <p class="brand-name">Toward Bright<span class="brand-line--large">MORROW</span></p>
    </div>
  </section>

  <section class="card card--back" aria-label="Card back">
    <div class="back-texture" role="img" aria-label="Light apricot background with a repeating pattern of small outlined bubbles"></div>
    <div class="contact-disc">
      <h1 class="contact-name">MARTIN K. PARDO</h1>
      <p class="contact-role">Managing Director</p>
      <ul class="contact-lines">
        <li><span class="contact-label">P:</span> 202.555.0183</li>
        <li><span class="contact-label">E:</span> martin@towardbrightmorrow.example</li>
      </ul>
      <p class="contact-web">www.<span class="accent">towardbrightmorrow</span>.example</p>
    </div>
  </section>
</main>
</body>
</html>
```